Pelmora needs stationery design

We need desings for presentation cards and letter head for our company. It would be better that the letterhead uses our logo with white background and the presentation card the logo with the black background for the back of the card and the text (name, phone
Updates

Necesitas un par de días antes de escoger al ganador

Colors
0455a3
ec1f27
000000

Requirements
Must have
• Use company logo and colors

```html
<!DOCTYPE html>
<html lang="es">
<head>
<meta charset="UTF-8">
<title>Pelmora – Tarjeta de presentación</title>
<link href="https://fonts.googleapis.com/css2?family=Michroma&family=Lato:wght@400;700&display=swap" rel="stylesheet">
<style>
  :root {
    --brand-blue: #0455a3;
    --brand-red: #ec1f27;
    --brand-black: #000000;
    --card-black: #141414;
    --paper: #fbfbfb;
    --ink: #1c1c1c;
    --muted: #6b6b6b;
    --backdrop: #e4e4e4;
    --white: #ffffff;
  }
  * { box-sizing: border-box; margin: 0; padding: 0; }
  html, body {
    width: 1200px;
    height: 1200px;
    overflow: hidden;
    background: var(--backdrop);
  }
  .sheet {
    width: 1200px;
    height: 1200px;
    display: flex;
    flex-direction: column;
    align-items: center;
    justify-content: center;
    gap: 60px;
  }
  .card {
    position: relative;
    width: 840px;
    height: 480px;
    overflow: hidden;
    box-shadow: 0 6px 18px rgba(0,0,0,0.14);
  }

  /* Front */
  .card--front { background: var(--paper); }
  .front-bands {
    position: absolute;
    top: 0; left: 0;
    width: 840px; height: 120px;
  }
  .identity {
    position: absolute;
    top: 96px;
    left: 70px;
  }
  .wordmark {
    font-family: "Michroma", sans-serif;
    letter-spacing: 0.04em;
    color: var(--ink);
  }
  .identity .wordmark { font-size: 40px; }
  .person-name {
    margin-top: 14px;
    font-family: "Lato", sans-serif;
    font-size: 34px;
    color: #444444;
    padding-bottom: 6px;
    border-bottom: 3px solid #9a9a9a;
    display: inline-block;
  }
  .person-role {
    margin-top: 8px;
    font-family: "Michroma", sans-serif;
    font-size: 13px;
    letter-spacing: 0.22em;
    color: var(--muted);
  }
  .contact-list {
    position: absolute;
    left: 300px;
    top: 268px;
    list-style: none;
    display: flex;
    flex-direction: column;
    gap: 22px;
  }
  .contact-item {
    display: flex;
    align-items: center;
    gap: 18px;
    font-family: "Michroma", sans-serif;
    font-size: 18px;
    letter-spacing: 0.14em;
    color: var(--ink);
  }
  .contact-icon {
    width: 34px;
    height: 34px;
    flex: none;
  }

  /* Back */
  .card--back {
    background: var(--card-black);
    display: flex;
    align-items: center;
    justify-content: center;
  }
  .card--back .wordmark {
    font-size: 66px;
    color: var(--white);
  }
</style>
</head>
<body>
<main class="sheet">

  <section class="card card--front" aria-label="Anverso de la tarjeta">
    <svg class="front-bands" viewBox="0 0 840 120" aria-hidden="true">
      <rect x="0" y="0" width="840" height="14" fill="var(--brand-red)"/>
      <rect x="0" y="14" width="840" height="12" fill="var(--brand-blue)"/>
      <polygon points="0,26 70,26 0,86" fill="var(--brand-blue)"/>
    </svg>

    <div class="identity">
      <div class="wordmark">PELMORA</div>
      <div class="person-name">Lorem Ipsum</div>
      <div class="person-role">MANAGER</div>
    </div>

    <ul class="contact-list">
      <li class="contact-item">
        <svg class="contact-icon" viewBox="0 0 34 34" aria-hidden="true">
          <circle cx="17" cy="17" r="17" fill="var(--brand-red)"/>
          <path d="M11 9 l4 0 l1.5 4.5 l-2.5 1.8 a10 10 0 0 0 4.7 4.7 l1.8 -2.5 l4.5 1.5 l0 4 a2 2 0 0 1 -2 2 a15 15 0 0 1 -14 -14 a2 2 0 0 1 2 -2z" fill="var(--white)"/>
        </svg>
        <span>008 512 730 2941</span>
      </li>
      <li class="contact-item">
        <svg class="contact-icon" viewBox="0 0 34 34" aria-hidden="true">
          <circle cx="17" cy="17" r="17" fill="var(--brand-red)"/>
          <path d="M17 8 a6.5 6.5 0 0 1 6.5 6.5 c0 4.5 -6.5 11 -6.5 11 s-6.5 -6.5 -6.5 -11 A6.5 6.5 0 0 1 17 8z" fill="var(--white)"/>
          <circle cx="17" cy="14.5" r="2.4" fill="var(--brand-red)"/>
        </svg>
        <span>DIRECCIÓN CALLE /14-B</span>
      </li>
      <li class="contact-item">
        <svg class="contact-icon" viewBox="0 0 34 34" aria-hidden="true">
          <circle cx="17" cy="17" r="17" fill="var(--brand-red)"/>
          <g fill="none" stroke="var(--white)" stroke-width="1.8">
            <circle cx="17" cy="17" r="8"/>
            <ellipse cx="17" cy="17" rx="3.5" ry="8"/>
            <line x1="9" y1="17" x2="25" y2="17"/>
          </g>
        </svg>
        <span>WWW.PELMORA.COM</span>
      </li>
      <li class="contact-item">
        <svg class="contact-icon" viewBox="0 0 34 34" aria-hidden="true">
          <circle cx="17" cy="17" r="17" fill="var(--brand-red)"/>
          <rect x="9" y="11.5" width="16" height="11" fill="var(--white)"/>
          <polyline points="9,11.5 17,18 25,11.5" fill="none" stroke="var(--brand-red)" stroke-width="1.6"/>
        </svg>
        <span>CONTACTO@PELMORA.COM</span>
      </li>
    </ul>
  </section>

  <section class="card card--back" aria-label="Reverso de la tarjeta">
    <div class="wordmark">PELMORA</div>
  </section>

</main>
</body>
</html>
```